Business Card Design Project

Doctor, Pain Management. Need a new business card design with appointment info on the back. New address is 18 Birchwood Court, Suite 304, Holloway, NJ 07519. Right now I believe the rest of the information is staying the same.

```html
<!DOCTYPE html>
<html lang="en">
<head>
<meta charset="utf-8">
<title>Steady Relief Pain Care – Business Card</title>
<link rel="stylesheet" href="https://fonts.googleapis.com/css2?family=Roboto+Condensed:wght@300;400;700&display=swap">
<style>
  :root {
    --backdrop: #5e4329;
    --card-dark: #17181a;
    --card-mid: #232427;
    --card-sheen: #3a3c40;
    --name-blue: #4fb8ea;
    --accent-yellow: #e7e437;
    --text-light: #e9ebee;
    --icon-blue: #5fc6f2;
    --divider: #6a6d72;
    --deco-blue: rgba(90, 130, 150, 0.22);
    --deco-gold: rgba(150, 140, 70, 0.16);
  }
  * { box-sizing: border-box; margin: 0; padding: 0; }
  html, body { width: 1200px; height: 950px; overflow: hidden; }
  body {
    background: var(--backdrop);
    font-family: "Roboto Condensed", "Arial Narrow", sans-serif;
    position: relative;
  }
  .card {
    position: absolute;
    left: 240px;
    width: 720px;
    height: 411px;
    border-radius: 4px;
    overflow: hidden;
    background: linear-gradient(135deg, var(--card-sheen) 0%, var(--card-mid) 30%, var(--card-dark) 100%);
    box-shadow: 0 10px 24px rgba(0,0,0,0.45);
  }
  .card--front { top: 50px; }
  .card--back { top: 490px; }

  .card__pattern {
    position: absolute;
    border-radius: 50%;
    filter: blur(6px);
  }
  .card--front .card__pattern {
    left: 20px; top: 140px; width: 520px; height: 260px;
    background: radial-gradient(ellipse at 40% 50%, var(--deco-blue) 0%, var(--deco-gold) 45%, transparent 72%);
  }
  .card--back .card__pattern {
    left: 140px; top: -40px; width: 560px; height: 260px;
    background: radial-gradient(ellipse at 55% 50%, var(--deco-blue) 0%, rgba(90,130,150,0.08) 50%, transparent 75%);
  }

  /* Front */
  .brand {
    position: absolute;
    left: 56px;
    top: 258px;
    display: flex;
    align-items: center;
    gap: 12px;
  }
  .brand__dot {
    width: 14px; height: 14px;
    border-radius: 50%;
    background: var(--icon-blue);
  }
  .brand__name {
    font-weight: 300;
    font-size: 24px;
    color: var(--accent-yellow);
    letter-spacing: 0.5px;
  }
  .card__divider {
    position: absolute;
    left: 370px;
    top: 40px;
    width: 1px;
    height: 200px;
    background: linear-gradient(to bottom, transparent, var(--divider) 25%, var(--divider) 75%, transparent);
  }
  .doctor {
    position: absolute;
    left: 400px;
    top: 56px;
  }
  .doctor__name {
    font-weight: 700;
    font-size: 30px;
    color: var(--name-blue);
    text-transform: uppercase;
    letter-spacing: 0.3px;
  }
  .doctor__title {
    font-weight: 700;
    font-size: 20px;
    color: var(--accent-yellow);
    margin-top: 2px;
  }
  .contact {
    list-style: none;
    margin-top: 26px;
  }
  .contact__item {
    display: flex;
    align-items: center;
    gap: 10px;
    font-size: 17px;
    color: var(--text-light);
    line-height: 1.55;
  }
  .contact__icon { width: 14px; height: 14px; flex: none; }

  /* Back */
  .practice {
    position: absolute;
    left: 60px;
    top: 250px;
  }
  .practice__name {
    font-weight: 300;
    font-size: 40px;
    color: var(--accent-yellow);
    letter-spacing: 1px;
  }
  .practice__rule {
    width: 430px;
    height: 2px;
    background: var(--accent-yellow);
    margin: 6px 0 8px;
  }
  .practice__address {
    font-size: 18px;
    color: var(--text-light);
    line-height: 1.45;
  }
</style>
</head>
<body>
  <section class="card card--front" aria-label="Business card front">
    <div class="card__pattern" role="img" aria-label="Faint decorative swirl and dot pattern"></div>
    <div class="brand">
      <span class="brand__dot"></span>
      <span class="brand__name">Steady Relief Pain Care</span>
    </div>
    <div class="card__divider"></div>
    <div class="doctor">
      <h1 class="doctor__name">Lianwen Zhou, M.D., Ph.D.</h1>
      <p class="doctor__title">Board Certified Anesthesiologist</p>
      <ul class="contact">
        <li class="contact__item">
          <svg class="contact__icon" viewBox="0 0 14 14"><path d="M3 1l2.2 2.6-1.3 1.6c.8 1.8 2.1 3.1 3.9 3.9l1.6-1.3L12 10l-1.3 2.4C5.7 12.2 1.8 8.3 1.6 3.3z" fill="var(--icon-blue)"/></svg>
          555.204.3186
        </li>
        <li class="contact__item">
          <svg class="contact__icon" viewBox="0 0 14 14"><rect x="1" y="4" width="12" height="8" rx="1" fill="var(--icon-blue)"/><rect x="3.5" y="1.5" width="7" height="3.5" fill="var(--icon-blue)"/><rect x="3.5" y="7" width="7" height="1.4" fill="var(--card-dark)"/></svg>
          555.204.3190
        </li>
        <li class="contact__item">
          <svg class="contact__icon" viewBox="0 0 14 14"><rect x="1" y="3" width="12" height="8.5" rx="1" fill="var(--icon-blue)"/><path d="M1.5 3.6L7 8l5.5-4.4" stroke="var(--card-dark)" stroke-width="1.3" fill="none"/></svg>
          reliefcare.desk@example.com
        </li>
        <li class="contact__item">
          <svg class="contact__icon" viewBox="0 0 14 14"><circle cx="7" cy="7" r="6" fill="var(--icon-blue)"/><path d="M1.5 7h11M7 1.2c-2.2 3.6-2.2 8 0 11.6M7 1.2c2.2 3.6 2.2 8 0 11.6" stroke="var(--card-dark)" stroke-width="1" fill="none"/></svg>
          www.steadyreliefcare.com
        </li>
      </ul>
    </div>
  </section>

  <section class="card card--back" aria-label="Business card back">
    <div class="card__pattern" role="img" aria-label="Faint decorative swirl and dot pattern"></div>
    <div class="practice">
      <h2 class="practice__name">Steady Relief Pain Care</h2>
      <div class="practice__rule"></div>
      <p class="practice__address">18 Birchwood Court, Suite 304, Holloway, NJ 07519</p>
      <p class="practice__address">62 Alder Road, Suite 9 Westbrook, NJ 07188</p>
    </div>
  </section>
</body>
</html>
```